Vimsa gifts app, mini-website

We have designed and launched an app to sell gift cards (a card with monetary value) and greeting cards (think penbrook paper cards made digital).

Target Market(s)

anyone who would buy and send gift cards via an app

Coding

Coded - Design and coding required

Number of Pages Required

1 page

```html
<!DOCTYPE html>
<html lang="en">
<head>
<meta charset="UTF-8">
<title>Vimsa Gifts</title>
<link href="https://fonts.googleapis.com/css2?family=Poppins:wght@400;500;600;700;800&family=Titillium+Web:wght@600;700&display=swap" rel="stylesheet">
<style>
:root{
  --red:#9c0a0c;
  --red-mid:#b22222;
  --red-light:#c1272d;
  --pink:#f8aeae;
  --pink-soft:#fbd3dc;
  --ink:#1a1a1a;
  --grey-band:#eceef1;
  --white:#ffffff;
  --black:#050505;
}
*{box-sizing:border-box;margin:0;padding:0}
html,body{width:1200px;height:3429px;overflow:hidden;background:var(--white)}
body{font-family:"Poppins",sans-serif;color:var(--ink)}
.page{position:relative;width:1200px;height:3429px;overflow:hidden}
.abs{position:absolute}

/* hero */
.hero-bg{position:absolute;left:0;top:0}
.brand{position:absolute;display:flex;align-items:center;gap:12px;font-family:"Poppins",sans-serif;font-weight:700;color:var(--white);font-size:26px;letter-spacing:1px}
.brand-mark{width:30px;height:30px;background:var(--white);border-radius:4px}
.main-nav{position:absolute;top:42px;right:107px;display:flex;gap:34px}
.main-nav a,.footer-nav a{font-family:"Titillium Web",sans-serif;font-weight:700;font-size:17px;color:var(--white);text-decoration:none;text-transform:uppercase}
.hero-title{position:absolute;left:110px;top:184px;font-weight:700;font-size:58px;line-height:68px;color:var(--white)}
.hero-text{position:absolute;left:111px;top:342px;width:410px;font-size:16px;line-height:30px;color:var(--white)}
.btn{position:absolute;display:flex;align-items:center;justify-content:center;font-family:"Poppins",sans-serif;font-weight:700;font-size:15px;text-transform:uppercase;text-decoration:none;border-radius:3px}
.btn-light{background:var(--white);color:var(--red-mid)}
.btn-red{background:var(--red-mid);color:var(--white)}
.hero-art{left:600px;top:82px;width:585px;height:625px;border-radius:40% 30% 30% 40%;background:radial-gradient(circle at 35% 30%,#ff8a8a 0%,#e8434a 35%,#f4a341 60%,rgba(255,255,255,0) 78%)}

/* about */
.about-art{left:0;top:738px;width:565px;height:506px;background:linear-gradient(120deg,#e4e4e4 0%,#cfcfcf 35%,#f7b9d3 55%,#f49bc0 80%,rgba(255,255,255,0) 100%);border-radius:0 40px 40px 0}
.section-title{position:absolute;font-weight:700;font-size:38px;color:var(--red-mid);text-transform:uppercase}
.about-text{position:absolute;left:601px;top:856px;width:485px;font-size:15.5px;line-height:30px;color:var(--ink)}

/* services */
.services{left:0;top:1268px;width:1200px;height:610px;background:linear-gradient(160deg,#f4f5f7 0%,#e3e5e9 40%,#f3f4f6 60%,#e1e3e7 100%)}
.service-card{position:absolute;top:1483px;width:273px;height:260px}
.service-panel{position:absolute;left:0;top:124px;width:100%;height:136px;background:var(--pink);border-radius:0 0 18px 18px}
.service-img{position:absolute;left:12px;top:2px;width:249px;height:124px;border-radius:10px 10px 0 0}
.service-frame{position:absolute;left:12px;top:0;width:249px;height:248px;border:2px solid #2a2a2a;border-radius:10px}
.service-body{position:absolute;left:20px;right:20px;top:142px;text-align:center}
.service-body h3{font-size:17px;font-weight:700;text-transform:uppercase;margin-bottom:6px}
.service-body p{font-size:16px;line-height:19.5px}
.service-card.active .service-panel{background:var(--red);box-shadow:0 14px 24px rgba(120,0,0,.35)}
.service-card.active .service-body{color:var(--white)}
.service-card.active .pointer{position:absolute;left:120px;top:106px;width:0;height:0;border-left:18px solid transparent;border-right:18px solid transparent;border-bottom:20px solid var(--red)}

/* cta */
.cta{left:0;top:1876px;width:1200px;height:446px;background:radial-gradient(ellipse at 50% 30%,#c2262b 0%,#a8141a 55%,#8e0b10 100%)}
.cta-title{position:absolute;left:0;top:1982px;width:1200px;text-align:center;font-weight:700;font-size:44px;line-height:53px;color:var(--white);text-transform:uppercase}
.dots{position:absolute;left:590px;top:2276px;display:flex;gap:12px}
.dots span{width:7px;height:7px;border-radius:50%;background:rgba(255,255,255,.55)}
.dots span:last-child{background:var(--white)}

/* contact */
.contact-card{left:197px;top:2401px;width:810px;height:586px;background:var(--white);box-shadow:0 4px 24px rgba(0,0,0,.09)}
.field{position:absolute;left:263px;width:345px;border:1.5px solid #555;background:var(--white);font-size:15px;padding:14px 21px;color:#333}
.send{position:absolute;left:263px;top:2884px;width:346px;height:37px;background:var(--red-mid);color:var(--white);font-weight:600;font-size:15px;display:flex;align-items:center;justify-content:center}
.contact-line{position:absolute;left:645px;display:flex;align-items:center;gap:16px;font-size:17.5px;font-weight:500}
.contact-line svg{width:18px;height:18px}
.socials{position:absolute;left:648px;top:2695px;display:flex;gap:26px}
.socials span{width:16px;height:16px;border-radius:50%;background:var(--red-mid)}
.map{left:645px;top:2747px;width:298px;height:174px;background:linear-gradient(135deg,#6f9fbe 0%,#8db3c9 35%,#d9c9a0 55%,#c7b58a 70%,#7fa9c4 100%)}
.gift-art{left:958px;top:2856px;width:182px;height:184px;border-radius:24px;background:linear-gradient(145deg,#f6b23a 0%,#e8353b 45%,#c9171d 100%);transform:rotate(-12deg)}

/* footer */
.footer-nav{position:absolute;top:3271px;left:0;width:1200px;display:flex;justify-content:center;gap:34px}
.copyright{position:absolute;left:113px;top:3364px;color:var(--white);font-size:15px}
</style>
</head>
<body>
<div class="page">

  <!-- hero -->
  <svg class="hero-bg" width="1200" height="660" viewBox="0 0 1200 660" aria-hidden="true">
    <path d="M0 0 H1200 V470 C1100 520 930 520 820 560 C680 615 470 650 320 622 C210 600 110 570 0 552 Z" fill="#9c0a0c"/>
    <path d="M380 0 H1200 V420 C1050 330 880 300 720 300 C560 300 470 240 420 140 C400 90 385 40 380 0 Z" fill="#b52427" opacity=".55"/>
  </svg>

  <div class="brand" style="left:110px;top:48px"><span class="brand-mark"></span>VIMSA</div>
  <nav class="main-nav">
    <a href="#">Home</a><a href="#">About</a><a href="#">Services</a><a href="#">Contact Us</a>
  </nav>

  <h1 class="hero-title">WELCOME TO<br>VIMSA GIFTS</h1>
  <p class="hero-text">Lorem ipsum dolor sit amet, consectetur adipiscing elit, sed do eiusmod tempor incididunt ut labore et dolore magna aliqua.</p>
  <a class="btn btn-light" href="#" style="left:113px;top:456px;width:133px;height:40px">Get Started</a>

  <div class="abs hero-art" role="img" aria-label="Phone showing the Vimsa gifts app surrounded by gift boxes and heart balloons"></div>

  <!-- about -->
  <div class="abs about-art" role="img" aria-label="Two greeting cards tied with ribbons, a grey father's day card and a pink mother's day card"></div>
  <h2 class="section-title" style="left:604px;top:780px">About Us</h2>
  <p class="about-text">Sed ut perspiciatis unde omnis iste natus error sit voluptatem accusantium doloremque laudantium, totam rem aperiam, eaque ipsa quae ab illo invesunt explicabo. Nemo enim ipsam voluptatem quia voluptas sit aspernatur aut odit aut fugit, sed quia consequuntur magni dolores eos qui ratione voluptatem sequi nesciunt. Neque porro quisquam est, qui dolorem ipsum quia dolor sit amet, consectetur, adipisci velit, sed quia non numquam eius modi tempora</p>
  <a class="btn btn-red" href="#" style="left:601px;top:1131px;width:132px;height:41px">Read More</a>

  <!-- services -->
  <div class="abs services"></div>
  <h2 class="section-title" style="left:0;top:1373px;width:1200px;text-align:center">Our Services</h2>

  <div class="service-card" style="left:149px">
    <div class="service-panel"></div>
    <div class="service-img" role="img" aria-label="Pink envelope with a handwritten tag" style="background:linear-gradient(135deg,#f9d6c9,#f3a7a9)"></div>
    <div class="service-frame"></div>
    <div class="service-body"><h3>Recipient</h3><p>Sed ut perspiciatis unde omnis iste natus error sit voluptatem accusan</p></div>
  </div>

  <div class="service-card active" style="left:463px">
    <div class="service-panel"></div>
    <div class="service-img" role="img" aria-label="Colourful new year greeting card" style="background:linear-gradient(90deg,#f2b233,#e0582f,#c63a55,#3f4f9a)"></div>
    <div class="pointer"></div>
    <div class="service-frame"></div>
    <div class="service-body"><h3>Greeting Card</h3><p>Sed ut perspiciatis unde omnis iste natus error sit voluptatem accusan</p></div>
  </div>

  <div class="service-card" style="left:777px">
    <div class="service-panel"></div>
    <div class="service-img" role="img" aria-label="Hand holding a gift card with a bow" style="background:linear-gradient(135deg,#bfe3f5,#9fd0ea 60%,#e9a98c)"></div>
    <div class="service-frame"></div>
    <div class="service-body"><h3>Gift Card</h3><p>Sed ut perspiciatis unde omnis iste natus error sit voluptatem accusan</p></div>
  </div>

  <!-- call to action -->
  <div class="abs cta"></div>
  <h2 class="cta-title">Copmlete your order and<br>select a delevery<br>method for your digital gift</h2>
  <a class="btn btn-light" href="#" style="left:533px;top:2191px;width:133px;height:40px">Get Started</a>
  <div class="dots"><span></span><span></span></div>

  <!-- contact -->
  <div class="abs contact-card"></div>
  <h2 class="section-title" style="left:197px;top:2450px;width:810px;text-align:center">Get in Touch</h2>
  <div class="field" style="top:2545px;height:52px">Name</div>
  <div class="field" style="top:2614px;height:52px">Email</div>
  <div class="field" style="top:2682px;height:174px">Your Message</div>
  <div class="send">SEND</div>

  <div class="contact-line" style="top:2539px">
    <svg viewBox="0 0 24 24" fill="none" stroke="#1a1a1a" stroke-width="2"><rect x="3" y="5" width="18" height="14" rx="2"/><path d="M3 7l9 6 9-6"/></svg>hello@vimsagifts.app
  </div>
  <div class="contact-line" style="top:2590px">
    <svg viewBox="0 0 24 24" fill="#1a1a1a"><path d="M6.6 10.8a15 15 0 006.6 6.6l2.2-2.2a1 1 0 011-.25 11.4 11.4 0 003.6.57 1 1 0 011 1V20a1 1 0 01-1 1A17 17 0 013 4a1 1 0 011-1h3.5a1 1 0 011 1c0 1.25.2 2.45.57 3.57a1 1 0 01-.25 1z"/></svg>+1 555 014 2297
  </div>
  <div class="contact-line" style="top:2638px">
    <svg viewBox="0 0 24 24" fill="#1a1a1a"><path d="M12 2a6 6 0 00-6 6c0 4.5 6 14 6 14s6-9.5 6-14a6 6 0 00-6-6zm0 8.5A2.5 2.5 0 1112 5.5a2.5 2.5 0 010 5z"/></svg>Lorem ipsum dolor
  </div>
  <div class="socials" aria-label="Social links"><span></span><span></span><span></span><span></span><span></span></div>
  <div class="abs map" role="img" aria-label="World map showing delivery coverage"></div>
  <div class="abs gift-art" role="img" aria-label="Red gift box with a golden bow"></div>

  <!-- footer -->
  <svg class="abs" style="left:0;top:3020px" width="1200" height="409" viewBox="0 0 1200 409" aria-hidden="true">
    <path d="M0 95 C180 20 380 0 580 45 C780 92 980 85 1200 10 V409 H0 Z" fill="#050505"/>
  </svg>
  <div class="brand" style="left:0;top:3180px;width:1200px;justify-content:center"><span class="brand-mark" style="background:#c1272d"></span>VIMSA GIFTS</div>
  <nav class="footer-nav">
    <a href="#">Home</a><a href="#">About</a><a href="#">Services</a><a href="#">Contact Us</a>
  </nav>
  <p class="copyright">© 2023 Vimsa gifts</p>

</div>
</body>
</html>
```